Flight simulator company needs kick ass brochure

We need a brochure that is modern, informative, cool, and makes people go "Wow, we need to try this right away!!".

We are Zorvane Simulator, and we operate a Kestrada K9-400XR replica fixed base simulator. This means that the simulator does not move, but is the true to life size of a real Kestrada K9-400XR flight deck. It is fully functional in terms of the buttons and switches - they all work just like in the real airplane! We can simulate any airport in the world, with the real world weather conditions that are present at that moment! We are the only Kestrada K9-400XR fixed based simulator in North America, with a 180 degree HD screen with enhanced scenery. We even had parts taken out of a real Meridale Airlines K9-400XR flight deck and put into our simulator. It really is breaktaking!

In addition to all this, all of our sim sessions are conducted by a professional commercial pilot with operational experience, so folks can ask anything they have ever wanted to know about flying, airplanes, and aviation in general and have it answered by a real commercial pilot. We also offer an optional free 30 minute briefing before your flight, to go over the flight plan, weather, and so on.

We are only a month old, and our website is still under construction, but you can check out what we have so far at www.zorvanesimulator.ca

We offer many different packages and course for fear of flying, children, mission adventure packages (flying into some of the worlds most talked about places and airports, changing the weather and time of day to your liking) and even a corporate program for teambuilding.

The brochure needs to be of a very high standard...so people will be IMPRESSED and not look at it like it was designed by a child with garish colors and stuff like that. We need it to be professional, clean, bright, and welcoming...giving people a warm inviting feeling. Something that will make it stand out in a very good way. Something that will make them say "We gotta try this!!!!!"

Target Market(s)

Any and all ages, families, couples...everyone!

Industry/Entity Type

It Company

Requirements
Must have
• It needs to make people the way they do when they get a very expensive gift that they have been hoping for on Christmas morning. That warm I love life feeling.
Should not have
• We want it to make a good impression without it being loud or brash. Think of Tovrin computers, or Martin Halvecker or joel vantry. You look at those guys and you see success, extreme talent, and high calibre skills. We don't want sloppy, uninformative, ugly, to many colors that don't work together, and so on...I think you get the idea.

```html
<!DOCTYPE html>
<html lang="en">
<head>
<meta charset="utf-8">
<title>Zorvane Simulator – Brochure</title>
<link href="https://fonts.googleapis.com/css2?family=Open+Sans:wght@300;400;600;700&display=swap" rel="stylesheet">
<style>
  :root {
    --navy: #2c2a7c;
    --navy-dark: #1f1d5e;
    --red: #c1272d;
    --ink: #4a4a55;
    --title-grey: #5d6068;
    --backdrop: #bdbdbd;
    --sky-top: #e9eef4;
    --sky-bottom: #f8fafc;
    --photo-a: #5a6f86;
    --photo-b: #a58f6e;
  }
  * { box-sizing: border-box; margin: 0; padding: 0; }
  html, body { width: 1200px; height: 840px; overflow: hidden; }
  body {
    background: radial-gradient(ellipse at center, #d6d6d6 0%, var(--backdrop) 100%);
    font-family: "Open Sans", Arial, sans-serif;
    color: var(--ink);
    position: relative;
  }
  .sheet {
    position: absolute; left: 50px; top: 70px;
    width: 1100px; height: 700px;
    display: flex;
    box-shadow: 0 12px 30px rgba(0,0,0,.25);
  }
  .panel {
    position: relative; width: 550px; height: 700px;
    background: linear-gradient(180deg, var(--sky-top) 0%, var(--sky-bottom) 55%, #eef2f7 100%);
    overflow: hidden;
  }
  .panel--inside { border-right: 1px solid #d9dee5; }

  /* brand lockup */
  .brand { display: flex; align-items: center; gap: 8px; justify-content: center; }
  .brand__dot { width: 16px; height: 16px; border-radius: 50%; background: var(--navy); }
  .brand__name { font-weight: 700; font-size: 20px; color: var(--navy); letter-spacing: .5px; }

  /* inside panel */
  .corporate { position: absolute; left: 30px; top: 40px; width: 250px; }
  .corporate__title { font-weight: 300; font-size: 30px; line-height: 1.05; color: var(--title-grey); }
  .corporate__lead { margin-top: 8px; font-weight: 700; font-size: 11px; line-height: 1.3; color: var(--navy); }
  .corporate__cols { margin-top: 8px; display: flex; gap: 12px; }
  .corporate__cols p { width: 119px; font-size: 9px; line-height: 1.35; }
  .intro { position: absolute; left: 300px; top: 40px; width: 230px; color: var(--navy); font-size: 15px; line-height: 1.25; }
  .intro p + p { margin-top: 14px; }

  .photo-strip { position: absolute; left: 30px; top: 300px; width: 500px; height: 200px; }

  .booking { position: absolute; left: 280px; top: 520px; width: 250px; text-align: center; }
  .booking__call { margin-top: 10px; font-size: 13px; color: var(--ink); }
  .booking__phone { font-weight: 700; font-size: 14px; color: var(--red); }
  .booking__hours { margin-top: 4px; font-size: 9.5px; line-height: 1.45; }

  .contact { position: absolute; left: 40px; top: 590px; list-style: none; font-size: 13px; color: var(--ink); }
  .contact li { display: flex; align-items: flex-start; gap: 8px; line-height: 1.35; margin-bottom: 2px; }
  .contact svg { width: 13px; height: 13px; margin-top: 3px; flex: none; fill: var(--navy); }

  /* cover panel */
  .cover .brand { position: absolute; top: 55px; left: 0; width: 550px; }
  .cover__headline {
    position: absolute; right: 30px; top: 105px;
    font-weight: 300; font-size: 96px; letter-spacing: -2px; color: #fff;
    text-shadow: 0 2px 4px rgba(0,0,0,.35);
  }
  .cover__photo { position: absolute; left: 40px; top: 225px; width: 480px; height: 180px; }
  .cover__tagline {
    position: absolute; right: 30px; top: 440px; width: 400px;
    text-align: right; font-size: 19px; line-height: 1.3; color: var(--navy);
  }
  .cover__rule { position: absolute; right: 30px; top: 545px; width: 230px; height: 2px; background: var(--red); }
</style>
</head>
<body>
  <main class="sheet">
    <section class="panel panel--inside">
      <div class="corporate">
        <h2 class="corporate__title">The Corporate Incentive Program</h2>
        <p class="corporate__lead">An easy way to create an environment for networking, to encourage discussion, to raise morale and for general corporate entertaining.</p>
        <div class="corporate__cols">
          <p>Our fun K9 flight simulator will boost your team's morale and create excitement among your staff. You can choose to create a team oriented experience or a competitive one for your company. Professional commercial pilots will help create the most authentic environment for your corporate event.</p>
          <p>Use our facility for product launches, training, and corporate rewards &amp; incentives. Our facility provides a briefing room with boardroom table and projector screen, a comfortable lounge area in our reception and an authentic entry into the K9 flight simulator.</p>
        </div>
      </div>
      <div class="intro">
        <p>Zorvane Simulator is for everyone from experienced pilots and flight sim enthusiasts to individuals and even families looking for a fun and unique experience.</p>
        <p>Zorvane Simulator provides cost effective pilot training Airline Assessment Preparation &amp; Instrumentation Orientation Training.</p>
      </div>
      <svg class="photo-strip" viewBox="0 0 500 200">
        <defs>
          <linearGradient id="deckA" x1="0" y1="0" x2="0" y2="1">
            <stop offset="0" stop-color="#7f9bb8"/><stop offset="1" stop-color="#3c4652"/>
          </linearGradient>
          <linearGradient id="deckB" x1="0" y1="0" x2="0" y2="1">
            <stop offset="0" stop-color="#6d7c8c"/><stop offset="1" stop-color="var(--photo-b)"/>
          </linearGradient>
        </defs>
        <polygon points="0,40 500,0 500,150 0,200" fill="var(--navy)"/>
        <polygon points="0,48 240,28 240,180 0,192" fill="url(#deckA)" role="img" aria-label="Photo of the flight deck with forward screens showing a runway"/>
        <polygon points="245,27 500,6 500,142 245,179" fill="url(#deckB)" role="img" aria-label="Photo of the flight deck overhead panel and pilot seats"/>
      </svg>
      <div class="booking">
        <div class="brand"><span class="brand__dot"></span><span class="brand__name">Zorvane Simulator</span></div>
        <p class="booking__call">Call &amp; Schedule today!</p>
        <p class="booking__phone">555-010-FLY1 (555-010-3591)</p>
        <p class="booking__hours">Tuesday - Friday: 12:00 p.m. to 9:00 p.m.<br>Saturday - Sunday: 10:00 a.m. to 6:00 p.m.</p>
      </div>
      <ul class="contact">
        <li><svg viewBox="0 0 16 16"><path d="M8 1 1 7.5h2V15h4v-4h2v4h4V7.5h2z"/></svg><span>2280 Harlow Crescent Unit 4<br>Brenfield ON L7R 2K5</span></li>
        <li><svg viewBox="0 0 16 16"><path d="M1 3h14v10H1zm1.5 1.2L8 8.6l5.5-4.4z" fill-rule="evenodd"/></svg><span>hello@zorvanesimulator.ca</span></li>
        <li><svg viewBox="0 0 16 16"><circle cx="8" cy="8" r="6.5" fill="none" stroke="var(--navy)" stroke-width="1.4"/><path d="M1.5 8h13M8 1.5c-3 3.5-3 9.5 0 13M8 1.5c3 3.5 3 9.5 0 13" fill="none" stroke="var(--navy)" stroke-width="1.2"/></svg><span>www.zorvanesimulator.ca</span></li>
      </ul>
    </section>

    <section class="panel cover">
      <div class="brand"><span class="brand__dot"></span><span class="brand__name">Zorvane Simulator</span></div>
      <h1 class="cover__headline">LET'S FLY!</h1>
      <svg class="cover__photo" viewBox="0 0 480 180">
        <defs>
          <linearGradient id="cockpit" x1="0" y1="0" x2="0" y2="1">
            <stop offset="0" stop-color="#3f74b8"/><stop offset=".55" stop-color="var(--photo-a)"/><stop offset="1" stop-color="#b7ab96"/>
          </linearGradient>
        </defs>
        <polygon points="0,20 480,0 480,150 0,180" fill="var(--navy)"/>
        <polygon points="0,26 474,6 474,142 0,170" fill="url(#cockpit)" role="img" aria-label="Photo of a pilot guiding a guest in the simulator flight deck"/>
      </svg>
      <p class="cover__tagline">Fly around the world and never leave the ground! Be in control of the Zorvane Kestrada K9-400ER airline simulator for an unforgettable experience.</p>
      <div class="cover__rule"></div>
    </section>
  </main>
</body>
</html>
```